Ward Compass Business Card Design*

We need a business card design for our company Ward Compass. Our company is specialized in providing online consulting services regarding medical institutions, hospitals and doctors. We work with patients worldwide looking to choose between healthcare providers. We have a website you may use as a reference, where we list doctors and clinics worldwide. So we target Medical providers as well as patients worldwide.
Target Market(s)
Medical Providers and patients around the world
Industry/Entity Type
Medical
Contact Information for Business Card
Salma Derkaoui
CEO
+90 612 348 2071
info@wardcompass-example.com
www.wardcompass-example.com
14 Annakhil 3 H.R.B. Rabat, Morocco
Requirements
Must have
- Company logo/name on one full side, personal info and smaller logo and company name on the other side.
Nice to have
- Smart and elegant design

```html
<!DOCTYPE html>
<html lang="en">
<head>
<meta charset="utf-8">
<title>Ward Compass – Business Card</title>
<link rel="stylesheet" href="https://fonts.googleapis.com/css2?family=Fira+Sans:wght@400;500&family=Merriweather:wght@400;700&display=swap">
<style>
  :root {
    --navy: #1c4370;
    --paper: #d4d4d4;
    --paper-line: #c9c9c9;
    --lime: #b6d334;
    --ink-light: #e3e6ea;
    --stage: #8b8b8b;
  }
  * { margin: 0; padding: 0; box-sizing: border-box; }
  html, body { width: 1200px; height: 800px; overflow: hidden; }
  body {
    background: var(--stage);
    font-family: "Fira Sans", sans-serif;
    display: flex;
    align-items: center;
    justify-content: center;
    gap: 40px;
  }
  .card {
    position: relative;
    width: 540px;
    height: 309px;
    overflow: hidden;
    box-shadow: 0 14px 30px rgba(0,0,0,.28);
  }

  /* Front */
  .card--front { background: var(--paper); }
  .front-brand {
    position: absolute;
    left: 0; right: 0; top: 96px;
    display: flex; align-items: center; justify-content: center; gap: 16px;
  }
  .front-brand__dot {
    width: 44px; height: 44px; border-radius: 50%;
    background: var(--navy);
  }
  .front-brand__name {
    font-weight: 500; font-size: 40px; letter-spacing: 1px;
    color: var(--navy);
  }
  .front-band {
    position: absolute; left: 0; right: 0; bottom: 0; height: 62px;
    background: var(--navy);
    display: flex; align-items: center; justify-content: center; gap: 12px;
    color: var(--ink-light); font-size: 16px; letter-spacing: .5px;
  }
  .front-band__slash { color: var(--lime); font-size: 20px; }

  /* Back */
  .card--back { background: var(--navy); }
  .back-lines { position: absolute; inset: 0; }
  .name-tab {
    position: absolute; left: 0; top: 30px;
    height: 42px; width: 300px;
    background: var(--paper);
    border-radius: 0 21px 21px 0;
    display: flex; align-items: center; padding-left: 22px;
  }
  .name-tab__name {
    font-family: "Merriweather", serif; font-weight: 700;
    font-size: 22px; color: var(--navy); letter-spacing: .3px;
  }
  .role {
    position: absolute; left: 24px; top: 88px;
    font-family: "Merriweather", serif; font-size: 15px;
    color: var(--ink-light); letter-spacing: 1px;
  }
  .contact {
    position: absolute; right: 22px; top: 168px;
    list-style: none;
    display: flex; flex-direction: column; gap: 5px;
    color: var(--ink-light); font-size: 12px;
  }
  .contact__item { display: flex; align-items: center; justify-content: flex-end; gap: 8px; }
  .contact__icon { width: 16px; height: 16px; flex: none; }
  .back-brand {
    position: absolute; right: 22px; bottom: 18px;
    display: flex; align-items: center; gap: 8px;
  }
  .back-brand__dot { width: 18px; height: 18px; border-radius: 50%; background: var(--ink-light); }
  .back-brand__name { font-weight: 500; font-size: 15px; color: var(--ink-light); letter-spacing: .5px; }
</style>
</head>
<body>

  <section class="card card--front" aria-label="Card front">
    <div class="front-brand">
      <span class="front-brand__dot"></span>
      <span class="front-brand__name">Ward Compass</span>
    </div>
    <div class="front-band">
      <span class="front-band__slash">/</span>
      <span>www.wardcompass-example.com</span>
      <span class="front-band__slash">/</span>
    </div>
  </section>

  <section class="card card--back" aria-label="Card back">
    <svg class="back-lines" width="540" height="309" viewBox="0 0 540 309" aria-hidden="true">
      <path d="M20 70 L20 84 L34 70 Z" fill="var(--paper)"/>
      <path d="M300 62 L518 62 L518 148 L500 148 L493 156 L486 148 L470 148"
            fill="none" stroke="var(--paper-line)" stroke-width="1.2"/>
    </svg>

    <div class="name-tab"><span class="name-tab__name">Salma Derkaoui</span></div>
    <p class="role">CEO</p>

    <ul class="contact">
      <li class="contact__item">+90 612 348 2071
        <svg class="contact__icon" viewBox="0 0 16 16"><circle cx="8" cy="8" r="8" fill="var(--ink-light)"/><path d="M5.5 4.2l1.6-.3.8 2-1 .8a5 5 0 0 0 2.3 2.3l.8-1 2 .8-.3 1.6c-3.6.2-6.4-2.6-6.2-6.2z" fill="var(--navy)"/></svg>
      </li>
      <li class="contact__item">info@wardcompass-example.com
        <svg class="contact__icon" viewBox="0 0 16 16"><circle cx="8" cy="8" r="8" fill="var(--ink-light)"/><rect x="4" y="5.2" width="8" height="5.6" fill="none" stroke="var(--navy)" stroke-width="1"/><path d="M4 5.2l4 3 4-3" fill="none" stroke="var(--navy)" stroke-width="1"/></svg>
      </li>
      <li class="contact__item">www.wardcompass-example.com
        <svg class="contact__icon" viewBox="0 0 16 16"><circle cx="8" cy="8" r="8" fill="var(--ink-light)"/><circle cx="8" cy="8" r="4.2" fill="none" stroke="var(--navy)" stroke-width="1"/><ellipse cx="8" cy="8" rx="1.8" ry="4.2" fill="none" stroke="var(--navy)" stroke-width=".9"/><path d="M3.8 8h8.4" stroke="var(--navy)" stroke-width=".9"/></svg>
      </li>
      <li class="contact__item">14 Annakhil 3 H.R.B. Rabat, Morocco
        <svg class="contact__icon" viewBox="0 0 16 16"><circle cx="8" cy="8" r="8" fill="var(--ink-light)"/><path d="M8 12.5s-3.2-3.4-3.2-5.6a3.2 3.2 0 0 1 6.4 0c0 2.2-3.2 5.6-3.2 5.6z" fill="var(--navy)"/><circle cx="8" cy="6.9" r="1.2" fill="var(--ink-light)"/></svg>
      </li>
    </ul>

    <div class="back-brand">
      <span class="back-brand__dot"></span>
      <span class="back-brand__name">Ward Compass</span>
    </div>
  </section>

</body>
</html>
```